Delicious BBQ Sauce package design!

We need a corner-pouch doypack (see attached) design that aligns with our logo (which is a cartoon and intended to depict a fun and delicious bbq sauce) and can accommodate three variants of the sauce (maybe just changing the name of the sauce and adding a slight visual differentiator?). The design needs to include the following:
1. "Spicin' it up since '96!" as banner
2. Logo
3. Name of sauce (as the differentiator. There are three): Harbor Glaze, Cobalt Glaze, Meadow Glaze
4. "Zesty and Tangy BBQ Sauce"
5. Actual image of bbq sauce (close up, not in container) as background to entire package. Samples attached. Let me know if you have a better idea!
6. UPC code (different for each sauce variant)
7. Company URL: www.dunmorebrisket.com
8. Splash for "First Place Sauce Winner at TWRA event!" with small image of the trophy. Attached.
9. Nutrition panel and ingredients
10. QR Code

Also open to your suggestions to make this packaging great!

Target Market(s)

People who love bbq sauce

Industry/Entity Type

Retail

Font styles to use
Sans Serif

Colors

Designer to choose colors to be used in the design.

Requirements
Must have
• The design needs to include the following:
• 1. "Spicin' it up since '96!" as banner
• 2. Logo
• 3. Name of sauce (as the differentiator. There are three): Harbor Glaze, Cobalt Glaze, Meadow Glaze
• 4. "Zesty and Tangy BBQ Sauce"
• 5. Actual image of bbq sauce (close up, not in container) as background to entire package. Samples attached. Let me know if you have a better idea!
• 6. UPC code (different for each sauce variant)
• 7. Company URL: www.dunmorebrisket.com
• 8. Splash for "First Place Sauce Winner at TWRA event!" with small image of the trophy. Attached.
• 9. Nutrition panel and ingredients
• 10. QR Code
Nice to have
• Open to suggestions that will make packaging appealing and will get people to buy it.

```html
<!DOCTYPE html>
<html lang="en">
<head>
<meta charset="utf-8">
<title>Dunmore Brisket BBQ Sauce – Harbor Glaze Pouch</title>
<link rel="stylesheet" href="https://fonts.googleapis.com/css2?family=Bebas+Neue&family=Oswald:wght@500;700&family=Yellowtail&display=swap">
<style>
  :root {
    --stage: #d9d9d9;
    --maroon-deep: #2e0303;
    --maroon: #5a0808;
    --crimson: #9a1114;
    --gold: #e9b12a;
    --amber: #f3a21c;
    --cream: #f4efe6;
    --sauce-dark: #8c1206;
    --sauce: #d8300c;
    --sauce-bright: #f0541a;
  }
  * { box-sizing: border-box; margin: 0; padding: 0; }
  html, body { width: 1200px; height: 1200px; overflow: hidden; background: var(--stage); }
  .canvas { position: relative; width: 1200px; height: 1200px; }

  .pouch-face {
    position: absolute; left: 290px; top: 155px; width: 620px; height: 890px;
    overflow: hidden;
    background: radial-gradient(ellipse at 50% 40%, var(--maroon-deep) 0%, var(--maroon) 65%, var(--crimson) 100%);
  }
  .decor { position: absolute; inset: 0; width: 620px; height: 890px; }

  .since-banner {
    position: absolute; left: 345px; top: 34px;
    font-family: 'Bebas Neue', 'Oswald', sans-serif; font-size: 28px; line-height: 1;
    color: var(--cream); letter-spacing: 0.5px; white-space: nowrap;
    transform: rotate(17deg); transform-origin: left center;
  }

  .brand { position: absolute; left: 0; right: 0; top: 128px; text-align: center; }
  .brand-mark {
    width: 118px; height: 118px; margin: 0 auto; border-radius: 50%;
    background: radial-gradient(circle at 45% 40%, #e7a63a 0%, #c24c1a 70%, #8a1a0c 100%);
    border: 3px solid var(--crimson);
  }
  .brand-name {
    margin-top: 8px; font-family: 'Oswald', sans-serif; font-weight: 700;
    font-size: 28px; line-height: 1.1; color: var(--gold); letter-spacing: 0.5px;
  }

  .title-frame {
    position: absolute; left: 130px; top: 351px; width: 362px; height: 136px;
    border: 2px solid var(--cream); border-radius: 6px; text-align: center;
  }
  .tagline {
    position: absolute; left: 50%; top: -26px; transform: translateX(-50%);
    padding: 0 10px; background: var(--maroon-deep);
    font-family: 'Yellowtail', cursive; font-size: 42px; color: var(--cream); white-space: nowrap; line-height: 1.1;
  }
  .tagline .joiner { font-size: 16px; color: var(--gold); margin: 0 2px; }
  .product-type {
    margin-top: 28px; font-family: 'Bebas Neue', sans-serif; font-size: 92px;
    line-height: 1; color: var(--gold); letter-spacing: 2px;
  }
  .variant-name {
    position: absolute; left: 0; right: 0; top: 500px; text-align: center;
    font-family: 'Bebas Neue', sans-serif; font-size: 58px; line-height: 1; color: var(--cream); letter-spacing: 1.5px;
  }

  .sauce-photo {
    position: absolute; left: 0; right: 0; top: 585px; bottom: 0;
    background:
      radial-gradient(ellipse at 30% 40%, var(--sauce-bright) 0%, transparent 45%),
      radial-gradient(ellipse at 75% 70%, var(--sauce-bright) 0%, transparent 40%),
      linear-gradient(180deg, var(--sauce-dark) 0%, var(--sauce) 30%, #b2200a 100%);
    -webkit-mask-image: linear-gradient(180deg, transparent 0%, #000 10%);
            mask-image: linear-gradient(180deg, transparent 0%, #000 10%);
  }
</style>
</head>
<body>
<main class="canvas">
  <section class="pouch-face">
    <svg class="decor" viewBox="0 0 620 890" aria-hidden="true">
      <path class="banner-swoop" d="M250 46 C380 40 520 80 620 150 L620 170 C520 105 390 66 250 58 Z" fill="var(--amber)"/>
    </svg>
    <div role="img" aria-label="Flame artwork sweeping from the spout corner"
         style="position:absolute;left:0;top:70px;width:200px;height:210px;border-radius:0 60% 60% 0;background:radial-gradient(ellipse at 10% 60%, #f3a21c 0%, #c21a14 45%, transparent 75%);"></div>
    <div role="img" aria-label="Flame artwork along the right edge"
         style="position:absolute;right:0;top:460px;width:160px;height:180px;border-radius:60% 0 0 60%;background:radial-gradient(ellipse at 95% 50%, #f3a21c 0%, #c21a14 45%, transparent 75%);"></div>

    <p class="since-banner">SPICIN' IT UP SINCE '96!</p>

    <div class="brand">
      <div class="brand-mark"></div>
      <p class="brand-name">Dunmore Brisket</p>
    </div>

    <div class="title-frame">
      <p class="tagline">Zesty<span class="joiner">And</span>Tangy</p>
      <h1 class="product-type">BBQ SAUCE</h1>
    </div>
    <h2 class="variant-name">HARBOR GLAZE</h2>

    <div class="sauce-photo" role="img" aria-label="Close-up photo of thick red BBQ sauce"></div>
  </section>
</main>
</body>
</html>
```